Brand Design/Redesign

Design and/or redesign an identity for product and organisation
Create visual identity (colours, fonts), website, mobile app, web application, online campaigns, social media.

I have given a sample wireframe for you to use so that we can really get a sense of the colour palette you are choosing and how it will look in a live context.

Considerations when Choosing:
Brand is for Gen Z -
With a particular focus on 16 - 18 years old.

There will be a commercial portal for Business to use also.

Please outline in a short paragraph why you choose the colours and their relationship to our target audience.

Selected winner to produce Brand Identity Document

Please see document attached.

Target Market(s)

Gen Z 16 - 18 yearolds

Industry/Entity Type

Social Media

Requirements
Must have
• Colour Palette & Font Selections, Visual of Colour Palette & Winner to produce Brand Identity Doc
Nice to have
• Really Cool, Edgy and Appeal to aYoung Audience
Should not have
• A corporate feel to it

```html
<!DOCTYPE html>
<html lang="en">
<head>
<meta charset="utf-8">
<title>Home – For you</title>
<link rel="stylesheet" href="https://fonts.googleapis.com/css2?family=Poppins:wght@400;500;600;700&display=swap">
<style>
  :root {
    --bg: #1b212d;
    --surface: #252c3a;
    --surface-hi: #2c3445;
    --line: #3a4356;
    --cyan: #1fe3e0;
    --cyan-deep: #0fb9c9;
    --text: #ffffff;
    --muted: #9aa3b5;
    --nav: #171c27;
    --accent-orange: #ff7a2f;
    --accent-violet: #6a35c9;
  }
  * { box-sizing: border-box; margin: 0; padding: 0; }
  html, body { width: 795px; height: 1200px; overflow: hidden; }
  body {
    background: var(--bg);
    color: var(--text);
    font-family: "Poppins", sans-serif;
    position: relative;
  }
  .status-bar {
    position: absolute; top: 0; left: 0; right: 0; height: 70px;
    display: flex; align-items: center; justify-content: space-between;
    padding: 0 48px; font-size: 22px; font-weight: 600;
  }
  .status-icons { display: flex; gap: 10px; align-items: center; }
  .search {
    position: absolute; top: 92px; left: 44px; right: 44px; height: 74px;
    background: var(--surface); border-radius: 20px;
    display: flex; align-items: center; gap: 18px; padding: 0 28px;
    color: var(--muted); font-size: 22px;
  }
  .tabs { position: absolute; top: 196px; left: 44px; display: flex; gap: 22px; }
  .tab {
    height: 50px; padding: 0 30px; border-radius: 25px;
    display: flex; align-items: center; font-size: 19px; font-weight: 500;
    border: 2px solid transparent; color: var(--text);
  }
  .tab.is-active { border-color: var(--cyan); color: var(--cyan); background: rgba(31,227,224,.08); }
  .challenge {
    position: absolute; top: 276px; left: 44px; right: 44px; height: 300px;
    border-radius: 26px; padding: 36px;
    background: linear-gradient(135deg, #2a3446 0%, #1f4a5a 100%);
    border: 2px solid rgba(31,227,224,.35);
  }
  .challenge h2 { font-size: 38px; font-weight: 600; margin-bottom: 14px; }
  .challenge p { font-size: 18px; line-height: 1.5; color: #d3d9e4; width: 340px; }
  .btn {
    display: inline-flex; align-items: center; justify-content: center;
    background: linear-gradient(90deg, var(--cyan), var(--cyan-deep));
    color: #0d2a33; font-weight: 600; border-radius: 12px;
  }
  .challenge .btn { margin-top: 26px; height: 56px; padding: 0 36px; font-size: 19px; }
  .challenge-art {
    position: absolute; right: 50px; top: 30px; width: 220px; height: 240px;
    border-radius: 50%;
    background: radial-gradient(circle, rgba(31,227,224,.55) 0%, rgba(31,227,224,.12) 50%, transparent 72%);
  }
  .stat-row { position: absolute; top: 604px; left: 44px; right: 44px; display: flex; gap: 22px; }
  .stat-card {
    flex: 1; height: 176px; background: var(--surface); border-radius: 22px; padding: 26px;
  }
  .greeting { font-size: 30px; font-weight: 500; margin-bottom: 24px; }
  .points-bar {
    height: 58px; border-radius: 14px; padding: 0 10px 0 20px;
    background: linear-gradient(90deg, var(--cyan), var(--cyan-deep));
    display: flex; align-items: center; justify-content: space-between;
    font-size: 26px; font-weight: 600; color: #fff;
  }
  .points-value { display: flex; align-items: center; gap: 10px; }
  .balance { font-size: 46px; font-weight: 600; color: var(--cyan); line-height: 1.1; }
  .earning { font-size: 19px; margin-top: 14px; color: #d3d9e4; }
  .earning strong { color: var(--text); font-weight: 600; }
  .earning-note { font-size: 15px; color: var(--muted); margin-top: 4px; }
  .section-head {
    position: absolute; top: 806px; left: 44px; right: 44px;
    display: flex; justify-content: space-between; align-items: center;
  }
  .section-head h3 { font-size: 32px; font-weight: 600; }
  .section-head a { color: var(--cyan); font-size: 19px; font-weight: 500; text-decoration: none; }
  .discover-row { position: absolute; top: 872px; left: 44px; right: 44px; display: flex; gap: 22px; }
  .discover-card {
    flex: 1; height: 210px; background: var(--surface); border-radius: 22px; padding: 24px;
  }
  .brand { display: flex; gap: 16px; align-items: flex-start; }
  .brand-mark { width: 52px; height: 52px; border-radius: 50%; background: var(--surface-hi); border: 2px solid var(--line); flex: none; }
  .brand-name { font-size: 24px; font-weight: 500; }
  .tags { font-size: 14px; color: var(--muted); line-height: 1.5; }
  .card-foot { display: flex; justify-content: space-between; align-items: flex-end; margin-top: 14px; }
  .pending-label { font-size: 15px; color: var(--muted); line-height: 1.3; }
  .pending-count { font-size: 30px; font-weight: 600; }
  .discover-card .btn { height: 42px; padding: 0 22px; font-size: 16px; color: #fff; }
  .square-mark { width: 50px; height: 50px; border-radius: 14px; background: linear-gradient(135deg, var(--accent-orange), var(--accent-violet)); }
  .sponsor { font-size: 15px; color: var(--muted); margin-top: 8px; }
  .action-title { font-size: 26px; font-weight: 600; line-height: 1.2; margin-top: 10px; }
  .remaining { display: flex; align-items: center; gap: 8px; font-size: 15px; color: var(--muted); margin-top: 10px; }
  .tab-bar {
    position: absolute; left: 0; right: 0; bottom: 0; height: 112px; background: var(--nav);
    display: flex; justify-content: space-around; align-items: center; padding-bottom: 8px;
  }
  .tab-item { display: flex; flex-direction: column; align-items: center; gap: 6px; font-size: 16px; color: var(--muted); }
  .tab-item.is-active { color: var(--cyan); }
  .tab-item svg { width: 30px; height: 30px; fill: none; stroke: currentColor; stroke-width: 2; stroke-linecap: round; stroke-linejoin: round; }
</style>
</head>
<body>
  <header class="status-bar">
    <span>9:20</span>
    <span class="status-icons">
      <svg width="26" height="18" viewBox="0 0 26 18" fill="#fff"><rect x="0" y="12" width="4" height="6" rx="1"/><rect x="7" y="8" width="4" height="10" rx="1"/><rect x="14" y="4" width="4" height="14" rx="1"/><rect x="21" y="0" width="4" height="18" rx="1"/></svg>
      <svg width="24" height="18" viewBox="0 0 24 18" fill="none" stroke="#fff" stroke-width="2.4" stroke-linecap="round"><path d="M2 6a15 15 0 0 1 20 0"/><path d="M6 10a9 9 0 0 1 12 0"/><circle cx="12" cy="15" r="1.6" fill="#fff"/></svg>
      <svg width="36" height="18" viewBox="0 0 36 18" fill="none"><rect x="1" y="1" width="30" height="16" rx="4" stroke="#fff" stroke-width="2"/><rect x="4" y="4" width="24" height="10" rx="2" fill="#fff"/><rect x="33" y="6" width="2.5" height="6" rx="1" fill="#fff"/></svg>
    </span>
  </header>

  <div class="search">
    <svg width="26" height="26" viewBox="0 0 24 24" fill="none" stroke="#9aa3b5" stroke-width="2.2" stroke-linecap="round"><circle cx="10.5" cy="10.5" r="7"/><path d="M16 16l5 5"/></svg>
    Search
  </div>

  <nav class="tabs">
    <span class="tab is-active">For you</span>
    <span class="tab">News</span>
  </nav>

  <section class="challenge">
    <h2>Daily Challenge</h2>
    <p>But I must explain to you how all mistaken idea of denouncing and praising pain</p>
    <span class="btn">Start now &gt;</span>
    <div class="challenge-art" role="img" aria-label="Glowing rocket launching illustration"></div>
  </section>

  <div class="stat-row">
    <section class="stat-card">
      <div class="greeting">Hi, Mira</div>
      <div class="points-bar">
        <span class="points-value">8
          <svg width="20" height="24" viewBox="0 0 20 24" fill="none" stroke="#fff" stroke-width="2.2"><path d="M10 2C6 8 3 12 3 15a7 7 0 0 0 14 0c0-3-3-7-7-13z"/></svg>
        </span>
        <svg width="40" height="40" viewBox="0 0 40 40" fill="none" stroke="#fff" stroke-width="2.4" stroke-linecap="round"><circle cx="20" cy="20" r="16"/><path d="M20 13v14M13 20h14"/></svg>
      </div>
    </section>
    <section class="stat-card">
      <div class="balance">$ 543</div>
      <div class="earning">Last earning: <strong>$120</strong></div>
      <div class="earning-note">Auto adjustment review</div>
    </section>
  </div>

  <div class="section-head">
    <h3>Discover</h3>
    <a href="#">More</a>
  </div>

  <div class="discover-row">
    <article class="discover-card">
      <div class="brand">
        <span class="brand-mark"></span>
        <div>
          <div class="brand-name">Stride Co</div>
          <div class="tags">#sport &nbsp;#lifestyle<br>#lifestyle</div>
        </div>
      </div>
      <div class="card-foot">
        <div>
          <div class="pending-label">Actions<br>pending</div>
          <div class="pending-count">233</div>
        </div>
        <span class="btn">Follow</span>
      </div>
    </article>
    <article class="discover-card">
      <span class="square-mark" style="display:block"></span>
      <div class="sponsor">Aerivo</div>
      <div class="action-title">My first action title</div>
      <div class="remaining">
        <svg width="16" height="16" viewBox="0 0 24 24" fill="none" stroke="#9aa3b5" stroke-width="2.2" stroke-linecap="round"><circle cx="12" cy="12" r="9"/><path d="M12 7v5l3 2"/></svg>
        05 days remaining
      </div>
    </article>
  </div>

  <nav class="tab-bar">
    <span class="tab-item is-active">
      <svg viewBox="0 0 24 24"><path d="M3 11l9-8 9 8v10H3z"/><path d="M9 21v-6h6v6"/></svg>Home
    </span>
    <span class="tab-item">
      <svg viewBox="0 0 24 24"><rect x="3" y="7" width="18" height="13" rx="2"/><path d="M8 7V5a4 4 0 0 1 8 0v2"/></svg>Marketplace
    </span>
    <span class="tab-item">
      <svg viewBox="0 0 24 24"><rect x="4" y="3" width="16" height="18" rx="2"/><path d="M4 9h16M10 13h4"/></svg>Vault
    </span>
    <span class="tab-item">
      <svg viewBox="0 0 24 24"><circle cx="12" cy="12" r="9"/><circle cx="12" cy="10" r="3"/><path d="M6.5 18a6 6 0 0 1 11 0"/></svg>Profile
    </span>
  </nav>
</body>
</html>
```